Riverbend Haven Home Care-Flyer for Patients

Our Home Health Care Agency, Riverbend Haven Home Care, is seeking a flyer to advertise our services. We would like our flyer to convey professionalism, classiness and sophistication. We want our agency to come across as one that is well-established and recognized as being first-rate within the field.

We also want to appear original; we want to stand out.

Our theme colors, blue and green, from our logo should be incorporated into the flyer's design (refer below).

The top of the page should say (in a clear, bold font)-Seeking Care for your Loved One?

Our Logo, followed by our slogan, "Let Your Neighbors Look After You", should be in the center. (This should make it appear as if our agency is the obvious solution to the consumer's quest in finding suitable care for their family member). This should be in a big font.
Below that, our agency's services should be listed in a very noticeable font...yet smaller than what's written above that.
The text should read:
Our Services Include:
*Experienced Certified Home Health Aides/ Live In Home Health Aides/Companions
*Nursing Services
*Alzheimer’s and Dementia Care
*Respite Care
*Postoperative Care
*Post Rehabilitation Care
*Running Errands
*Light Housekeeping
*Assistance with Bathing, Feeding and Grooming
*Meal Preparation
*Laundry and Linen Washing
*Mail and Bill Organization
*Medication Management
*Accompanying to Doctor’s Appointments
*And much more!
Below that, in a smaller, yet noticeable font:
As seasoned professionals, we know how to help our clients navigate and fulfill their various health care needs. Your Community is here to help you get the care that you deserve.
Call Riverbend Haven Home Care today to learn more about our first-rate services!
Below that, in a larger font, our phone number, website, our e-mail address.
*Out contact information will be provided to the project’s winner*.

*Pictures of Caregivers helping elderly patient should be included in the advertisement as well. *

We provided advertisements of other Home Health Care Agencies attached below to use as a reference. Once again, while we are aiming for a similar idea; however, our goal is to stand out as the community's premiere home health care agency, the one that they want to choose. We want to be original as well!

Size: Standard Computer Paper Size. 8.5” x 11”.

Feel free to utilize your creative, designer flair!
We look forward to seeing the results!
Good luck!

Industry/Entity Type

Home Health Care

Font styles to use
Sans Serif

Requirements
Must have
• Refer above.
Nice to have
• Refer to attachment below to see how other home health care agencies advertise. While we are aiming for a similar idea, we would like to incorporate our logo, slogan and colors to make this flyer more unique and stand out. We would like to appear original.

```html
<!DOCTYPE html>
<html lang="en">
<head>
<meta charset="utf-8">
<title>Riverbend Haven Home Care – Flyer</title>
<link rel="stylesheet" href="https://fonts.googleapis.com/css2?family=Alfa+Slab+One&family=Montserrat:wght@400;500;600;700&display=swap">
<style>
  :root {
    --page-bg: #e9e7ec;
    --royal: #264f94;
    --navy: #232f63;
    --ink: #1a1d22;
    --green: #8cc63f;
    --green-dark: #6fa52c;
    --teal: #a9dad2;
    --cream: #ebe7b6;
    --white: #ffffff;
    --text: #1f1f24;
  }
  * { box-sizing: border-box; margin: 0; padding: 0; }
  html, body {
    width: 1040px; height: 1200px; overflow: hidden;
    background: var(--page-bg);
    font-family: "Montserrat", sans-serif;
  }
  .flyer {
    position: absolute; left: 76px; top: 26px;
    width: 772px; height: 998px;
    transform: scale(1.15); transform-origin: top left;
    background: var(--royal);
    overflow: hidden;
  }
  .headline {
    position: absolute; top: 0; left: 0; width: 100%; height: 145px;
    text-align: center; font-family: "Alfa Slab One", serif;
    padding-top: 38px;
  }
  .headline .line-one { color: var(--white); font-size: 33px; letter-spacing: 0.5px; line-height: 42px; }
  .headline .line-two { color: var(--green); font-size: 41px; letter-spacing: 0.5px; line-height: 48px; }

  .hero { position: absolute; top: 145px; left: 0; width: 772px; height: 430px; }
  .hero svg { display: block; }

  .brand {
    position: absolute; top: 196px; left: 45px; width: 420px;
    text-align: center;
  }
  .brand .brand-dot {
    display: block; width: 78px; height: 78px; margin: 0 auto 14px;
    border-radius: 50%; background: var(--royal);
  }
  .brand .brand-name {
    color: var(--royal); font-weight: 600; font-size: 22px; line-height: 28px;
    text-transform: uppercase; letter-spacing: 0.3px; white-space: nowrap;
  }
  .brand .brand-tagline {
    margin-top: 6px; color: var(--royal); font-weight: 500; font-size: 12px;
    letter-spacing: 2.6px; text-transform: uppercase; white-space: nowrap;
  }

  .slogan {
    position: absolute; top: 577px; left: 0; width: 100%;
    text-align: center; color: var(--cream);
    font-weight: 700; font-size: 26px; letter-spacing: 1.4px; text-transform: uppercase;
  }
  .services-title {
    position: absolute; top: 616px; left: 32px;
    color: var(--green); font-weight: 600; font-size: 17px;
  }
  .service {
    position: absolute; height: 30px;
    background: var(--green); border-left: 4px solid var(--green-dark);
    color: var(--ink); font-weight: 600; font-size: 11px;
    display: flex; align-items: center; padding-left: 10px; white-space: nowrap;
  }
  .c1 { left: 32px; width: 233px; }
  .c2 { left: 270px; width: 273px; padding-left: 4px; }
  .c12 { left: 32px; width: 511px; }
  .c3 { left: 550px; width: 190px; padding-left: 18px; }
  .r1 { top: 640px; } .r2 { top: 677px; } .r3 { top: 711px; } .r4 { top: 746px; } .r5 { top: 780px; }

  .about {
    position: absolute; top: 825px; left: 0; width: 100%; height: 85px;
    background: var(--white); padding: 7px 32px 0;
    color: var(--text); font-size: 15.2px; line-height: 23px;
  }
  .contact-bar { position: absolute; top: 910px; left: 0; width: 100%; height: 88px; background: var(--navy); }
  .contact-bar .phone-panel {
    position: absolute; inset: 0 auto 0 0; width: 412px; background: var(--ink);
    clip-path: polygon(0 0, 100% 0, 88% 100%, 0 100%);
  }
  .phone {
    position: absolute; left: 30px; top: 24px;
    display: flex; align-items: center; gap: 16px;
    color: var(--white); font-weight: 600; font-size: 39px; letter-spacing: 0.5px;
  }
  .web-lines {
    position: absolute; right: 32px; top: 16px;
    color: var(--white); font-size: 17px; line-height: 31px; font-weight: 500;
  }
  .web-lines div { display: flex; align-items: center; gap: 9px; }
</style>
</head>
<body>
<main class="flyer">
  <header class="headline">
    <div class="line-one">SEEKING CARE FOR YOUR</div>
    <div class="line-two">LOVED ONES?</div>
  </header>

  <section class="hero">
    <svg width="772" height="430" viewBox="0 0 772 430">
      <defs>
        <linearGradient id="roomTone" x1="0" y1="0" x2="1" y2="1">
          <stop offset="0" stop-color="#f7f5f2"/>
          <stop offset="0.55" stop-color="#ebe4dc"/>
          <stop offset="1" stop-color="#cdbfb0"/>
        </linearGradient>
        <linearGradient id="heartTone" x1="0" y1="0" x2="1" y2="1">
          <stop offset="0" stop-color="#f2eeea"/>
          <stop offset="1" stop-color="#9fb4d4"/>
        </linearGradient>
      </defs>
      <rect role="img" aria-label="Photo of a caregiver helping a smiling elderly woman seated with a cane at home" x="0" y="0" width="772" height="430" fill="url(#roomTone)"/>
      <path d="M0,76 C70,220 230,425 430,428 C600,430 720,330 772,262 L772,430 L0,430 Z" fill="var(--teal)"/>
      <path d="M0,88 C70,228 228,418 428,421 C598,423 718,332 772,272 L772,430 L0,430 Z" fill="var(--royal)"/>
      <path role="img" aria-label="Photo of a caregiver checking on an elderly man, framed in a heart" d="M164,405 C120,370 60,330 60,290 C60,250 90,232 116,232 C140,232 156,246 164,262 C172,246 188,232 212,232 C238,232 263,250 263,290 C263,330 208,370 164,405 Z" fill="url(#heartTone)" stroke="var(--white)" stroke-width="5"/>
    </svg>
  </section>

  <div class="brand">
    <span class="brand-dot"></span>
    <div class="brand-name">Riverbend Haven Home Care</div>
    <div class="brand-tagline">Let your neighbors look after you</div>
  </div>

  <h2 class="slogan">Let Your Neighbors Look After You</h2>
  <h3 class="services-title">Our Services Include</h3>

  <div class="service c12 r1">Experienced Certified Home Health Aides/ Live In Home Health Aides /Companions</div>
  <div class="service c3 r1">Respite Care</div>
  <div class="service c1 r2">Post Rehabilitation Care</div>
  <div class="service c2 r2">Nursing Services</div>
  <div class="service c3 r2">Post Operative Care</div>
  <div class="service c1 r3">Alzeimer's and Dementia Care</div>
  <div class="service c2 r3">Assistance with Bathing, Feeding &amp; Grooming</div>
  <div class="service c3 r3">Meal Preparation</div>
  <div class="service c1 r4">Laundry and Linen Washing</div>
  <div class="service c2 r4">Light Housekeeping</div>
  <div class="service c3 r4">Mail and Bill Organization</div>
  <div class="service c1 r5">Running Errands</div>
  <div class="service c2 r5">Accompanying to Doctor's Appointments</div>
  <div class="service c3 r5">Medication Management</div>

  <p class="about">As seasoned professionals, we know how to help our clients navigate and fulfill their various health care needs. Your Community is here to help you get the care that you deserve. Call Riverbend Haven Home Care today to learn more about our first-rate services!</p>

  <footer class="contact-bar">
    <div class="phone-panel"></div>
    <div class="phone">
      <svg width="34" height="36" viewBox="0 0 24 24" aria-hidden="true"><path fill="#6ec3ee" d="M6.6 10.8a15.1 15.1 0 0 0 6.6 6.6l2.2-2.2a1 1 0 0 1 1-.25 11.4 11.4 0 0 0 3.6.57 1 1 0 0 1 1 1V20a1 1 0 0 1-1 1A17 17 0 0 1 3 4a1 1 0 0 1 1-1h3.5a1 1 0 0 1 1 1c0 1.250.2 2.45.57 3.57a1 1 0 0 1-.25 1z"/></svg>
      <span>1234 567 890</span>
    </div>
    <div class="web-lines">
      <div><svg width="10" height="10" viewBox="0 0 10 10" aria-hidden="true"><circle cx="5" cy="5" r="4" fill="none" stroke="#c8cde0" stroke-width="1"/><path d="M1 5h8M5 1v8" stroke="#c8cde0" stroke-width="0.8"/></svg>www.websiteaddress.com</div>
      <div><svg width="11" height="9" viewBox="0 0 11 9" aria-hidden="true"><rect x="0.5" y="0.5" width="10" height="8" fill="none" stroke="#c8cde0"/><path d="M0.5 0.5l5 4 5-4" fill="none" stroke="#c8cde0"/></svg>info@websiteaddress.com</div>
    </div>
  </footer>
</main>
</body>
</html>
```